Kestrel Homes Web Site Design

improve on the graphic design on our current website
www.kestrelhmoes.com.au
wordpress required

Industry/Entity Type

Graphic Design

Coding

Coded - Design and coding required

Number of Pages Required

5+ page

```html
<!DOCTYPE html>
<html lang="en">
<head>
<meta charset="utf-8">
<title>Kestrel Homes</title>
<link href="https://fonts.googleapis.com/css2?family=Roboto:wght@300;400;500;700&display=swap" rel="stylesheet">
<style>
:root{
  --red:#c41f30;
  --red-dark:#9e1626;
  --ink:#4a4a4a;
  --muted:#777;
  --white:#fff;
  --dark:#1c1c1e;
  --grey-band:#dcdcdc;
}
*{box-sizing:border-box;margin:0;padding:0}
html,body{width:1200px;height:3974px;overflow:hidden}
body{font-family:"Roboto",Arial,sans-serif;color:var(--ink);background:var(--white);position:relative}
section,header,footer{position:absolute;left:0;width:1200px;overflow:hidden}
.abs{position:absolute}
.fill{position:absolute;inset:0}

/* hero */
.hero{top:0;height:678px}
.hero .fill{background:linear-gradient(180deg,#2a2a2c 0%,#3b3836 45%,#1e1d1d 100%)}
.nav-home{left:77px;top:21px;width:114px;height:53px;border-radius:27px;background:var(--red);color:var(--white);font-size:17px;display:flex;align-items:center;justify-content:center}
.nav-item{top:36px;color:var(--white);font-size:17px;letter-spacing:.3px}
.social-top{top:20px;display:flex;gap:22px;left:994px;align-items:center}
.social-top .dot{width:50px;height:50px;border-radius:50%;background:var(--red)}
.social-top .plain{width:24px;height:24px;border-radius:50%;background:#d8d8d8}
.brand{left:0;width:1200px;top:180px;display:flex;justify-content:center;align-items:center;gap:22px}
.brand .mark{width:110px;height:110px;border-radius:50%;background:var(--red)}
.brand .name{font-size:92px;font-weight:500;color:#cfcfcf;letter-spacing:1px}
.brand-sub{left:0;width:1200px;top:312px;text-align:center;color:#cfcfcf;font-size:19px;padding-left:240px}
.service{width:260px;text-align:center;color:var(--white);font-size:18px;line-height:26px}
.service .ring{width:110px;height:110px;border-radius:50%;border:5px solid var(--white);background:var(--red);margin:0 auto 16px;display:flex;align-items:center;justify-content:center}

/* about */
.about{top:678px;height:403px;text-align:center}
.about .mark{left:570px;top:62px;width:60px;height:60px;border-radius:50%;border:3px solid #ccc}
.about h2{position:absolute;top:140px;width:100%;font-size:41px;font-weight:400;color:#555}
.accent{color:var(--red)}
.about p{position:absolute;left:125px;width:950px;top:196px;font-size:14px;line-height:22px;color:var(--muted)}
.btn{position:absolute;background:var(--red);color:var(--white);border-radius:30px;display:flex;align-items:center;justify-content:center;font-size:18px;font-weight:500}
.about .btn{left:506px;top:286px;width:188px;height:58px}

/* why */
.why{top:1081px;height:524px}
.why .fill{background:linear-gradient(90deg,#a8182a 0%,#b82737 50%,#8f1322 100%)}
.why .person{left:0;top:0;width:290px;height:524px;background:linear-gradient(180deg,#8a8a8a,#5a5e66 60%,#3d4350)}
.why h2{left:384px;top:60px;font-size:40px;font-weight:400;color:var(--white)}
.why .text{left:384px;top:126px;width:700px;font-size:14.5px;line-height:26px;color:#f3dcdf}
.why .sign{left:390px;top:255px;width:90px;height:62px;background:linear-gradient(90deg,rgba(255,255,255,.15),rgba(255,255,255,.05));border-radius:6px}
.stat-ring{width:116px;height:116px;border-radius:50%;background:var(--white);display:flex;align-items:center;justify-content:center}
.stat-num{font-size:46px;color:var(--white);font-weight:400}
.stat-label{font-size:16px;color:var(--white);letter-spacing:.5px}

/* testimonial */
.testimonial{top:1605px;height:366px;text-align:center}
.testimonial .fill{background:linear-gradient(180deg,#2b2b2d,#1a1a1b)}
.testimonial h2{position:absolute;top:60px;width:100%;font-size:40px;font-weight:300;color:#cfcfcf}
.quote-mark{left:580px;top:132px;font-size:80px;color:var(--white);font-weight:700;line-height:80px}
.testimonial p{position:absolute;left:212px;width:776px;top:196px;font-size:14.5px;line-height:23px;color:#d6d6d6}
.testimonial .who{position:absolute;top:290px;width:100%;font-size:15px;color:var(--red)}
.arrow{width:58px;height:58px;border-radius:50%;border:3px solid var(--white);display:flex;align-items:center;justify-content:center}

/* portfolio */
.portfolio{top:1971px;height:850px;text-align:center}
.portfolio h2{position:absolute;top:55px;width:100%;font-size:40px;font-weight:400;color:#555}
.filters{top:126px;left:0;width:1200px;display:flex;justify-content:center;gap:34px;align-items:center;font-size:16px;color:#555}
.filters .on{background:var(--red);color:var(--white);border-radius:22px;padding:12px 28px}
.tile{position:absolute}
.tile.t-a{background:linear-gradient(135deg,#cfd6de,#8c9aa8)}
.tile.t-b{background:linear-gradient(160deg,#d9d4cc,#7c7368)}
.tile.t-c{background:linear-gradient(160deg,#8fb3d6,#6d7a6a)}
.tile.hover{background:rgba(196,31,48,.9);display:flex;align-items:center;justify-content:center}
.portfolio .btn{left:520px;top:728px;width:160px;height:56px}

/* team */
.team{top:2821px;height:374px;background:var(--grey-band)}
.team h2{position:absolute;top:72px;width:100%;text-align:center;font-size:40px;font-weight:400;color:#555}
.member-photo{width:170px;height:170px;border-radius:50%;border:6px solid var(--white);background:linear-gradient(180deg,#9a9a9a,#4c4c4c)}
.member-name{font-size:18px;color:var(--red);font-weight:500}
.member-role{font-size:14px;color:#666;margin-top:6px}
.member-bio{font-size:14px;line-height:20px;color:#777;margin-top:14px;width:330px}
.member-more{font-size:14px;color:var(--red);margin-top:12px;font-weight:500}

/* contact */
.contact{top:3195px;height:641px}
.contact .fill{background:linear-gradient(180deg,#1d2430,#14161b 60%,#0e0f11)}
.contact h2{position:absolute;top:60px;width:100%;text-align:center;font-size:40px;font-weight:400;color:var(--white)}
.get-in-touch{left:262px;top:150px;color:var(--red);font-size:17px;font-weight:500}
.field{position:absolute;left:77px;width:572px;background:var(--white);color:#888;font-size:13px;padding:16px 18px}
.field.first{border-bottom:3px solid var(--red)}
.submit{left:275px;top:463px;width:106px;height:106px;border-radius:50%;background:var(--red);color:var(--white);font-size:18px;display:flex;align-items:center;justify-content:center;font-weight:500}
.contact-brand{left:660px;top:215px;display:flex;align-items:center;gap:14px}
.contact-brand .mark{width:58px;height:58px;border-radius:50%;background:#888}
.contact-brand .name{font-size:44px;color:#9a9a9a;font-weight:500}
.company{left:652px;top:320px;font-size:17px;color:var(--red);font-weight:500}
.info{left:652px;font-size:14px;color:#ddd;display:flex;gap:14px;align-items:flex-start;line-height:22px}
.info svg{flex:none;margin-top:3px}

/* footer */
.footer{top:3836px;height:138px;background:var(--red)}
.top-tab{left:556px;top:3788px;width:88px;height:48px}
.foot-dot{width:48px;height:48px;border-radius:50%;border:2px solid var(--white)}
.copyright{position:absolute;top:92px;width:100%;text-align:center;color:var(--white);font-size:13px}
</style>
</head>
<body>

<header class="hero">
  <div class="fill" role="img" aria-label="Photo of a dark modern kitchen and dining interior"></div>
  <div class="abs nav-home">HOME</div>
  <div class="abs nav-item" style="left:225px">COMPANY</div>
  <div class="abs nav-item" style="left:344px">EXCELLENCE</div>
  <div class="abs nav-item" style="left:482px">EXPERIENCE</div>
  <div class="abs nav-item" style="left:617px">EXPERTISE</div>
  <div class="abs nav-item" style="left:736px">CONTACT</div>
  <div class="abs social-top" aria-label="Social links">
    <span class="dot"></span><span class="plain"></span><span class="plain"></span>
  </div>
  <div class="abs brand"><span class="mark"></span><span class="name">Kestrel Homes</span></div>
  <div class="abs brand-sub">Home &amp; Designs Pty Ltd</div>

  <div class="abs service" style="left:201px;top:422px">
    <div class="ring"><svg width="56" height="50" viewBox="0 0 56 50"><path d="M4 24 L28 4 L52 24" fill="none" stroke="#fff" stroke-width="4"/><rect x="12" y="22" width="32" height="24" fill="#fff"/><rect x="24" y="32" width="8" height="14" fill="#c41f30"/></svg></div>
    CANBERRA BUILDING<br>SERVICES
  </div>
  <div class="abs service" style="left:474px;top:422px">
    <div class="ring"><svg width="54" height="54" viewBox="0 0 54 54"><path d="M8 46 L46 8" stroke="#fff" stroke-width="6"/><path d="M8 46 L8 30 L24 46 Z" fill="#fff"/><rect x="30" y="30" width="18" height="18" fill="none" stroke="#fff" stroke-width="3"/></svg></div>
    <span style="display:block;margin-top:16px">TOP CLASS ARCHITECTS</span>
  </div>
  <div class="abs service" style="left:763px;top:422px">
    <div class="ring"><svg width="60" height="50" viewBox="0 0 60 50"><rect x="6" y="34" width="40" height="10" rx="5" fill="#fff"/><rect x="14" y="18" width="22" height="14" fill="#fff"/><path d="M36 22 L50 10 L56 26" fill="none" stroke="#fff" stroke-width="4"/></svg></div>
    RELIABLE<br>CONTRACTORS
  </div>
</header>

<section class="about">
  <div class="abs mark"></div>
  <h2>ABOUT <span class="accent">KESTREL HOME &amp; DESIGNS PTY LTD</span></h2>
  <p>Kestrel believe in people and quality before profits it's quite selfish really-we know from experience that if our people are doing great work-our clients reap the rewards, and they in turn will reward us appropriately. Personal responsibility, individual ownership and a willingness to show initiative are attributes we support and expect from our people. All our employees follow our Code of Conduct.</p>
  <div class="btn">KNOW MORE</div>
</section>

<section class="why">
  <div class="fill" role="img" aria-label="Red tinted photo of a glass office interior"></div>
  <div class="abs person" role="img" aria-label="Photo of a smiling man in a grey shirt with arms crossed"></div>
  <h2 class="abs">WHY KESTREL HOMES ?</h2>
  <div class="abs text">Our vision is to build homes to the highest standards.<br>We're a boutique building company in Canberra, that has built many residential properties.<br>Being in the industry for many years has enabled us to master the art of designing and constructing stylish<br>homes that are not only aesthetically pleasing but also affordable.</div>
  <div class="abs sign" role="img" aria-label="Handwritten signature"></div>
  <div class="abs stat-ring" style="left:387px;top:347px"><svg width="60" height="56" viewBox="0 0 60 56"><path d="M4 28 L30 6 L56 28" fill="none" stroke="#c41f30" stroke-width="4"/><rect x="14" y="26" width="32" height="26" fill="none" stroke="#c41f30" stroke-width="4"/><rect x="26" y="36" width="8" height="16" fill="#c41f30"/></svg></div>
  <div class="abs stat-num" style="left:511px;top:352px">253+</div>
  <div class="abs stat-label" style="left:513px;top:414px">HOUSES WE BUILT</div>
  <div class="abs stat-ring" style="left:705px;top:347px;background:transparent;border:4px solid #fff"><svg width="60" height="56" viewBox="0 0 60 56"><circle cx="30" cy="18" r="10" fill="none" stroke="#fff" stroke-width="3"/><path d="M12 48 C12 34 48 34 48 48 Z" fill="none" stroke="#fff" stroke-width="3"/></svg></div>
  <div class="abs stat-num" style="left:837px;top:352px">18+</div>
  <div class="abs stat-label" style="left:840px;top:414px">PEOPLE IN OUR TEAM</div>
</section>

<section class="testimonial">
  <div class="fill" role="img" aria-label="Dark photo of a living room interior"></div>
  <h2>WHAT OUR <span class="accent">CLIENT SAY</span></h2>
  <div class="abs quote-mark">&ldquo;</div>
  <p>I've engaged Kestrel Homes to build my first house in Canberra, all I can say is they've been fantastic. Tom has helped me out at every stage of the building process, making sure everything was handled smoothly. Whenever I needed a change they've been very helpful.</p>
  <div class="who">- LAURA PENNINGTON</div>
  <div class="abs arrow" style="left:101px;top:186px"><svg width="18" height="22" viewBox="0 0 18 22"><path d="M14 2 L4 11 L14 20" fill="none" stroke="#fff" stroke-width="4"/></svg></div>
  <div class="abs arrow" style="left:1028px;top:186px"><svg width="18" height="22" viewBox="0 0 18 22"><path d="M4 2 L14 11 L4 20" fill="none" stroke="#fff" stroke-width="4"/></svg></div>
</section>

<section class="portfolio">
  <h2>OUR <span class="accent">PORTFOLIO</span></h2>
  <div class="abs filters"><span class="on">ALL</span><span>GALLERY</span><span>BUILDER</span><span>EXTENSIONS</span><span>BATHROOMS</span><span>REFURBISHMENT</span></div>

  <div class="tile hover" style="left:77px;top:199px;width:188px;height:164px" role="img" aria-label="Highlighted project tile"><svg width="50" height="50" viewBox="0 0 50 50"><path d="M25 5 V45 M5 25 H45" stroke="#fff" stroke-width="3"/></svg></div>
  <div class="tile t-a" style="left:275px;top:199px;width:358px;height:164px" role="img" aria-label="Photo of a white modern two storey house"></div>
  <div class="tile t-b" style="left:644px;top:199px;width:198px;height:164px" role="img" aria-label="Photo of a bright kitchen interior"></div>
  <div class="tile t-c" style="left:853px;top:199px;width:270px;height:164px" role="img" aria-label="Photo of a brick and render family home"></div>

  <div class="tile t-c" style="left:77px;top:376px;width:196px;height:162px" role="img" aria-label="Photo of a modern house with timber cladding"></div>
  <div class="tile t-a" style="left:283px;top:376px;width:265px;height:162px" role="img" aria-label="Photo of a white contemporary house"></div>
  <div class="tile t-b" style="left:559px;top:376px;width:270px;height:162px" role="img" aria-label="Photo of a house facade with balcony"></div>
  <div class="tile t-b" style="left:840px;top:376px;width:283px;height:162px" role="img" aria-label="Photo of a living room interior"></div>

  <div class="tile t-c" style="left:77px;top:548px;width:267px;height:164px" role="img" aria-label="Photo of a two storey townhouse"></div>
  <div class="tile t-a" style="left:355px;top:548px;width:201px;height:164px" role="img" aria-label="Photo of a white dining interior"></div>
  <div class="tile t-c" style="left:567px;top:548px;width:355px;height:164px" role="img" aria-label="Photo of a modern home at dusk"></div>
  <div class="tile t-a" style="left:932px;top:548px;width:191px;height:164px" role="img" aria-label="Photo of a grey rendered house"></div>

  <div class="btn">VIEW ALL</div>
</section>

<section class="team">
  <h2>OUR <span class="accent">TEAM</span></h2>
  <div class="abs member-photo" style="left:79px;top:140px" role="img" aria-label="Portrait photo of the CEO"></div>
  <div class="abs" style="left:268px;top:156px">
    <div class="member-name">GRAHAM WHITFIELD</div>
    <div class="member-role">CEO &amp; ARCHITECT</div>
    <div class="member-bio">Mauris accumsan eros eget libero posuere vulputate. Etiam elit elit, elementum sed varius at, adipiscing vitae est.</div>
    <div class="member-more">MORE --&gt;</div>
  </div>
  <div class="abs member-photo" style="left:601px;top:140px" role="img" aria-label="Portrait photo of the architect"></div>
  <div class="abs" style="left:789px;top:156px">
    <div class="member-name">MEGAN CALLOWAY</div>
    <div class="member-role">ARCHITECT</div>
    <div class="member-bio">Mauris accumsan eros eget libero posuere vulputate. Etiam elit elit, elementum sed varius at, adipiscing vitae est.</div>
    <div class="member-more">MORE --&gt;</div>
  </div>
</section>

<section class="contact">
  <div class="fill" role="img" aria-label="Dark night photo of a modern building"></div>
  <h2>CONTACT <span class="accent">US</span></h2>
  <div class="abs get-in-touch">GET IN TOUCH</div>
  <div class="field first" style="top:196px;height:52px">Enter Name:</div>
  <div class="field" style="top:257px;height:52px">Enter Phone no.:</div>
  <div class="field" style="top:318px;height:52px">Enter E-Mail:</div>
  <div class="field" style="top:381px;height:133px">Message:</div>
  <div class="abs submit">SUBMIT</div>

  <div class="abs contact-brand"><span class="mark"></span><span class="name">Kestrel Homes</span></div>
  <div class="abs company">KESTREL HOME &amp; DESIGNS PTY LTD</div>
  <div class="abs info" style="top:370px"><svg width="18" height="18" viewBox="0 0 18 18"><path d="M3 5 H15 M3 9 H15 M3 13 H15" stroke="#c41f30" stroke-width="2.5"/></svg><span>Canberra, ACT<br>14, Banksia Pl, Kingston</span></div>
  <div class="abs info" style="top:437px"><svg width="18" height="14" viewBox="0 0 18 14"><rect x="1" y="1" width="16" height="12" fill="#c41f30"/><path d="M1 1 L9 8 L17 1" fill="none" stroke="#fff" stroke-width="1.5"/></svg><span>tom@kestrelhomes.com.au</span></div>
  <div class="abs info" style="top:477px"><svg width="18" height="18" viewBox="0 0 18 18"><path d="M4 2 L7 2 L8 6 L6 7 C7 10 8 11 11 12 L12 10 L16 11 L16 14 C16 15 15 16 14 16 C8 16 2 10 2 4 C2 3 3 2 4 2 Z" fill="#c41f30"/></svg><span>0400 118 392</span></div>
</section>

<footer class="footer">
  <div class="abs" style="left:517px;top:26px;display:flex;gap:10px" aria-label="Social links">
    <span class="foot-dot"></span><span class="foot-dot"></span><span class="foot-dot"></span>
  </div>
  <div class="copyright">&copy;Kestrel Home Builders Canberra - 2016. All rights reserved.</div>
</footer>
<svg class="abs top-tab" viewBox="0 0 88 48"><path d="M0 48 L44 0 L88 48 Z" fill="#c41f30"/><path d="M34 30 L44 21 L54 30 M34 38 L44 29 L54 38" fill="none" stroke="#fff" stroke-width="3"/></svg>

</body>
</html>
```